TIMBER DECK COMPANY FLYER

We need a flyer design for a Timber Decking company, we specialise in timber decks, stairs, privacy screens, maintenance and pergolas. I have attatched some pictures which you can incorporate if you think they need cropping go for it. We offer amazing decks at affordable prices by qualified tradespeople.
My logo is a dull green I would like this to be changed to a more lime bright green please. Also my logo is too big I would like this logo halved in size please. And the colours in the brochure maybe a blackbackground with lime green and other colours you think will work. We will also beat any reputable Decking companies quote by 10%. Our decks add style, class, longjevity and practicality to any home. The final design should be modern and cutting edge.

Target Market(s)

home owners

Industry/Entity Type

It Company

Logo Text

CRISP PLANKWORKS GROUP

Requirements
Must have
• DECKS
STAIRS
PERGOLAS
PRIVACY SCREENS
DECK MAINTENANCE

CONTACT-GORDON-0438261507

MUST HAVE LIKE US ON PAGEBOARD LOGO

www.crispplankworksgroup.com.au
Nice to have
• Please let me know if need more photos etc

```html
<!DOCTYPE html>
<html lang="en">
<head>
<meta charset="utf-8">
<title>Crisp Plankworks Group Flyer</title>
<link href="https://fonts.googleapis.com/css2?family=Cinzel:wght@400;600&family=Open+Sans:wght@400&display=swap" rel="stylesheet">
<style>
  :root {
    --page-bg: #f2f2f2;
    --panel-light: #ececec;
    --panel-grey: #e4e4e6;
    --panel-dark: #231f20;
    --ink: #231f20;
    --lime: #6cc13f;
    --white: #ffffff;
    --timber-light: #c9a46a;
    --timber-red: #8a4a2e;
    --foliage: #3d5a2c;
    --pool: #1f3a38;
  }
  * { box-sizing: border-box; margin: 0; padding: 0; }
  html, body { width: 900px; height: 1200px; overflow: hidden; background: var(--page-bg); }
  .flyer {
    position: absolute; left: 35px; top: 13px;
    width: 830px; height: 1174px;
    background: var(--panel-grey);
    overflow: hidden;
    box-shadow: 0 2px 10px rgba(0,0,0,0.15);
  }
  .brand-panel {
    position: absolute; left: 0; top: 0; width: 472px; height: 286px;
    background: var(--panel-light);
  }
  .brand-mark {
    position: absolute; left: 26px; top: 56px; width: 72px; height: 72px;
    background: var(--lime);
  }
  .brand-name {
    position: absolute; left: 122px; top: 62px; width: 340px;
    font-family: "Open Sans", sans-serif; font-weight: 400;
    font-size: 25px; line-height: 31px; color: var(--ink);
    letter-spacing: 0.3px;
  }
  .tagline {
    position: absolute; left: 24px; top: 170px; width: 440px;
    font-family: "Open Sans", sans-serif; font-size: 32px; line-height: 40px;
    color: var(--ink);
  }
  .photo { position: absolute; }
  .photo-pool {
    left: 472px; top: 0; width: 358px; height: 286px;
    background: linear-gradient(160deg, #6d6a64 0%, var(--pool) 45%, var(--timber-red) 100%);
  }
  .photo-stairs {
    left: 0; top: 286px; width: 443px; height: 427px;
    background: linear-gradient(100deg, var(--foliage) 0%, #5b6e3a 35%, var(--timber-light) 70%, #b89460 100%);
  }
  .photo-deck {
    left: 472px; top: 901px; width: 358px; height: 273px;
    background: linear-gradient(175deg, #b6b2ad 0%, #8e4b2c 35%, #a75c35 70%, #4f6d33 100%);
  }
  .copy {
    position: absolute; left: 473px; width: 340px;
    font-family: "Cinzel", serif; font-weight: 400;
    font-size: 27px; line-height: 43px; color: var(--ink);
  }
  .copy-style { top: 312px; }
  .copy-beat { top: 516px; color: var(--lime); }
  .copy-offer { top: 722px; }
  .services {
    position: absolute; left: 0; top: 713px; width: 443px; height: 461px;
    background: var(--panel-dark); color: var(--white);
    font-family: "Cinzel", serif;
  }
  .services-title { position: absolute; left: 25px; top: 38px; font-size: 23px; }
  .service-list { position: absolute; left: 25px; top: 84px; list-style: none; }
  .service-list li {
    display: flex; align-items: center; height: 48px;
    font-size: 23px; letter-spacing: 0.3px;
  }
  .service-list svg { width: 26px; height: 22px; margin-right: 16px; }
  .contact { position: absolute; left: 25px; top: 315px; font-size: 20px; line-height: 31px; }
  .follow {
    position: absolute; left: 25px; top: 391px; display: flex; align-items: center;
    font-size: 18px; color: var(--lime);
  }
  .social-badge {
    display: flex; align-items: center; margin-left: 18px;
    background: var(--white); border-radius: 3px; padding: 4px 8px;
    font-size: 14px; color: var(--ink); font-weight: 600;
  }
  .social-badge .dot { width: 12px; height: 12px; background: var(--ink); margin-right: 6px; }
  .website {
    position: absolute; left: 25px; top: 428px;
    font-size: 15px; color: var(--lime); letter-spacing: 0.3px;
  }
</style>
</head>
<body>
<main class="flyer">
  <section class="brand-panel">
    <div class="brand-mark"></div>
    <div class="brand-name">CRISP PLANKWORKS<br>GROUP</div>
    <p class="tagline">Affordability&nbsp; Sustanability<br>Relaxability</p>
  </section>

  <div class="photo photo-pool" role="img" aria-label="Plunge pool surrounded by a red timber deck and sandstone garden beds"></div>
  <div class="photo photo-stairs" role="img" aria-label="Timber staircase with handrail beside leafy green shrubs"></div>

  <p class="copy copy-style">Our decks add style, class, longevity and practicality to any home.</p>
  <p class="copy copy-beat">We also beat any reputable Decking companies quote by 10%.</p>
  <p class="copy copy-offer">We offer amazing decks at affordable prices by qualified trades people.</p>

  <div class="photo photo-deck" role="img" aria-label="Freshly oiled hardwood deck in a backyard with a green plant in the corner"></div>

  <section class="services">
    <h2 class="services-title" style="font-weight:400">We specialise In</h2>
    <ul class="service-list">
      <li><svg viewBox="0 0 26 22"><path d="M2 12 L9 19 L24 2" fill="none" stroke="#fff" stroke-width="2.5"/></svg>Timber Decks</li>
      <li><svg viewBox="0 0 26 22"><path d="M2 12 L9 19 L24 2" fill="none" stroke="#fff" stroke-width="2.5"/></svg>Stairs</li>
      <li><svg viewBox="0 0 26 22"><path d="M2 12 L9 19 L24 2" fill="none" stroke="#fff" stroke-width="2.5"/></svg>Privacy Screens</li>
      <li><svg viewBox="0 0 26 22"><path d="M2 12 L9 19 L24 2" fill="none" stroke="#fff" stroke-width="2.5"/></svg>Maintenance &amp; Pergolas</li>
    </ul>
    <p class="contact">Contact<br>Gordon-0438261507</p>
    <div class="follow">Follow Us On
      <span class="social-badge"><span class="dot"></span>Pageboard</span>
    </div>
    <p class="website">www.crispplankworksgroup.com.au</p>
  </section>
</main>
</body>
</html>
```